New Candy Packaging Design

Looking to create an attractive design for modern retail for our single stick candy that will stand out on retail shelves. It will be hung from a whole. The design should have brand elements like the irregular shapes, bright pastel colors. Please visit pebblefrostcandy.example to ensure the product could be an extension of the product range. 3 colors, pink(sakura flavor), green(muscat grape flavor), and blue(french vanilla flavor).

Target Market(s)

Millenias and Genz

Industry/Entity Type

Food

Requirements
Must have
• Look and feel of brand extension for Pebbles, Matt finish
Nice to have
• fruit shapes
Should not have
• tacky design

```html
<!DOCTYPE html>
<html lang="en">
<head>
<meta charset="utf-8">
<title>Pebbles Rock Sugar Sticks – Packaging Range</title>
<link rel="stylesheet" href="https://fonts.googleapis.com/css2?family=Roboto+Slab:wght@400;700;800&family=Arimo:wght@400&display=swap">
<style>
  :root {
    --bg: #f3f1ee;
    --ink: #1f1f1f;
    --white: #ffffff;
    --sakura: #d63a84;
    --sakura-light: #ec6aa6;
    --sakura-dark: #b82a6c;
    --grape: #6d8f28;
    --grape-light: #8fae3e;
    --grape-dark: #557321;
    --vanilla: #2f6b9f;
    --vanilla-light: #4482b7;
    --vanilla-dark: #245784;
    --stick: #d9c09a;
    --stick-dark: #bfa37a;
    --brand-pink: #d64a9c;
  }
  * { margin: 0; padding: 0; box-sizing: border-box; }
  html, body { width: 1200px; height: 1170px; overflow: hidden; }
  body {
    background: var(--bg);
    position: relative;
    font-family: "Roboto Slab", serif;
  }
  .variant-label {
    position: absolute;
    top: 138px;
    width: 40px;
    text-align: center;
    font-family: "Arimo", sans-serif;
    font-size: 30px;
    color: var(--ink);
  }
  .pack {
    position: absolute;
    top: 179px;
    width: 242px;
    height: 777px;
  }
  .pack--sakura { left: 126px; }
  .pack--grape { left: 465px; }
  .pack--vanilla { left: 809px; }
  .pack text { font-family: "Roboto Slab", serif; fill: var(--white); }
  .pack .tagline { font-size: 11px; font-weight: 400; }
  .pack .brand-name { font-size: 46px; font-weight: 800; }
  .pack .flavor-name { font-size: 24px; font-weight: 400; letter-spacing: 1px; }
  .pack .flavor-strong { font-weight: 800; }
  .pack .flavor-small { font-size: 15px; }
  .pack .claim { font-size: 16px; letter-spacing: 0.5px; }
  .signature-logo {
    position: absolute;
    left: 968px;
    top: 1062px;
    color: var(--brand-pink);
    font-family: "Roboto Slab", serif;
    font-weight: 700;
    text-align: right;
    line-height: 1;
  }
  .signature-logo__tagline { font-size: 12px; display: block; margin-bottom: 2px; }
  .signature-logo__name { font-size: 58px; display: block; }
</style>
</head>
<body>

  <div class="variant-label" style="left:227px">A</div>
  <div class="variant-label" style="left:566px">B</div>
  <div class="variant-label" style="left:911px">C</div>

  <!-- Sakura flavour -->
  <svg class="pack pack--sakura" viewBox="0 0 242 777" aria-label="Pebbles Sakura Flavor rock sugar stick pack">
    <defs>
      <linearGradient id="sakura-body" x1="0" y1="0" x2="1" y2="1">
        <stop offset="0" stop-color="var(--sakura-light)"/>
        <stop offset="0.5" stop-color="var(--sakura)"/>
        <stop offset="1" stop-color="var(--sakura-dark)"/>
      </linearGradient>
      <linearGradient id="sakura-candy" x1="0" y1="0" x2="0" y2="1">
        <stop offset="0" stop-color="#f4c7c4"/>
        <stop offset="1" stop-color="#e79a92"/>
      </linearGradient>
      <path id="sakura-left" d="M121 562 A76 142 0 0 1 121 278"/>
      <path id="sakura-right" d="M184 560 Q200 420 184 280"/>
    </defs>
    <path d="M0 0 H242 V70 L228 86 V690 L242 706 V777 H0 V706 L14 690 V86 L0 70 Z" fill="url(#sakura-body)"/>
    <rect x="0" y="0" width="242" height="70" fill="var(--sakura-dark)" opacity="0.25"/>
    <circle cx="121" cy="25" r="12" fill="var(--bg)"/>
    <text class="tagline" x="130" y="114" text-anchor="middle">Rock Sugar Sticks</text>
    <text class="brand-name" x="121" y="160" text-anchor="middle">Pebbles</text>
    <rect role="img" aria-label="Illustration of pale pink cherry blossoms" x="45" y="172" width="150" height="66" rx="33" fill="#f3c6dc" opacity="0.8"/>
    <ellipse role="img" aria-label="Pink sakura rock sugar candy seen through window" cx="121" cy="420" rx="54" ry="113" fill="url(#sakura-candy)"/>
    <text class="flavor-name"><textPath href="#sakura-left" startOffset="50%" text-anchor="middle">SAKURA FLAVOR</textPath></text>
    <text class="claim"><textPath href="#sakura-right" startOffset="50%" text-anchor="middle">A CANDY &amp; MORE</textPath></text>
    <rect x="118" y="533" width="6" height="150" fill="var(--stick)"/>
    <circle cx="121" cy="690" r="11" fill="var(--stick-dark)"/>
    <rect role="img" aria-label="Illustration of cherry blossoms" x="140" y="706" width="102" height="71" rx="30" fill="#f3c6dc" opacity="0.8"/>
  </svg>

  <!-- Muscat grape flavour -->
  <svg class="pack pack--grape" viewBox="0 0 242 777" aria-label="Pebbles Muscat Grape Flavor rock sugar stick pack">
    <defs>
      <linearGradient id="grape-body" x1="0" y1="0" x2="1" y2="1">
        <stop offset="0" stop-color="var(--grape-light)"/>
        <stop offset="0.5" stop-color="var(--grape)"/>
        <stop offset="1" stop-color="var(--grape-dark)"/>
      </linearGradient>
      <linearGradient id="grape-candy" x1="0" y1="0" x2="0" y2="1">
        <stop offset="0" stop-color="#eef3c2"/>
        <stop offset="1" stop-color="#cfe39a"/>
      </linearGradient>
      <path id="grape-left" d="M121 562 A76 142 0 0 1 121 278"/>
      <path id="grape-right" d="M184 560 Q200 420 184 280"/>
    </defs>
    <path d="M0 0 H242 V70 L228 86 V690 L242 706 V777 H0 V706 L14 690 V86 L0 70 Z" fill="url(#grape-body)"/>
    <rect x="0" y="0" width="242" height="70" fill="var(--grape-dark)" opacity="0.25"/>
    <circle cx="121" cy="25" r="12" fill="var(--bg)"/>
    <text class="tagline" x="130" y="114" text-anchor="middle">Rock Sugar Sticks</text>
    <text class="brand-name" x="121" y="160" text-anchor="middle">Pebbles</text>
    <rect role="img" aria-label="Illustration of green muscat grapes with leaves" x="40" y="172" width="160" height="76" rx="36" fill="#c7dc8a" opacity="0.85"/>
    <ellipse role="img" aria-label="Pale green grape rock sugar candy seen through window" cx="121" cy="420" rx="54" ry="113" fill="url(#grape-candy)"/>
    <text class="flavor-name"><textPath href="#grape-left" startOffset="50%" text-anchor="middle"><tspan class="flavor-small">MUSCAT </tspan><tspan class="flavor-strong">GRAPE</tspan><tspan class="flavor-small"> FLAVOR</tspan></textPath></text>
    <text class="claim"><textPath href="#grape-right" startOffset="50%" text-anchor="middle">A CANDY &amp; MORE</textPath></text>
    <rect x="118" y="533" width="6" height="150" fill="var(--stick)"/>
    <circle cx="121" cy="690" r="11" fill="var(--stick-dark)"/>
    <rect role="img" aria-label="Illustration of halved green grapes" x="136" y="706" width="106" height="71" rx="32" fill="#c7dc8a" opacity="0.85"/>
  </svg>

  <!-- French vanilla flavour -->
  <svg class="pack pack--vanilla" viewBox="0 0 242 777" aria-label="Pebbles French Vanilla Flavor rock sugar stick pack">
    <defs>
      <linearGradient id="vanilla-body" x1="0" y1="0" x2="1" y2="1">
        <stop offset="0" stop-color="var(--vanilla-light)"/>
        <stop offset="0.5" stop-color="var(--vanilla)"/>
        <stop offset="1" stop-color="var(--vanilla-dark)"/>
      </linearGradient>
      <linearGradient id="vanilla-candy" x1="0" y1="0" x2="0" y2="1">
        <stop offset="0" stop-color="#3f9be6"/>
        <stop offset="1" stop-color="#1f6cc2"/>
      </linearGradient>
      <path id="vanilla-left" d="M121 562 A76 142 0 0 1 121 278"/>
      <path id="vanilla-right" d="M184 560 Q200 420 184 280"/>
    </defs>
    <path d="M0 0 H242 V70 L228 86 V690 L242 706 V777 H0 V706 L14 690 V86 L0 70 Z" fill="url(#vanilla-body)"/>
    <rect x="0" y="0" width="242" height="70" fill="var(--vanilla-dark)" opacity="0.25"/>
    <circle cx="121" cy="25" r="12" fill="var(--bg)"/>
    <text class="tagline" x="130" y="114" text-anchor="middle">Rock Sugar Sticks</text>
    <text class="brand-name" x="121" y="160" text-anchor="middle">Pebbles</text>
    <rect role="img" aria-label="Illustration of vanilla pods and a white vanilla flower" x="35" y="174" width="170" height="58" rx="28" fill="#5b4a3c" opacity="0.55"/>
    <ellipse role="img" aria-label="Blue vanilla rock sugar candy seen through window" cx="121" cy="410" rx="54" ry="113" fill="url(#vanilla-candy)"/>
    <text class="flavor-name"><textPath href="#vanilla-left" startOffset="50%" text-anchor="middle"><tspan class="flavor-small">FRENCH </tspan><tspan class="flavor-strong">VANILLA</tspan><tspan class="flavor-small"> FLAVOR</tspan></textPath></text>
    <text class="claim"><textPath href="#vanilla-right" startOffset="50%" text-anchor="middle">A CANDY &amp; MORE</textPath></text>
    <rect x="118" y="523" width="6" height="160" fill="var(--stick)"/>
    <circle cx="121" cy="690" r="11" fill="var(--stick-dark)"/>
    <rect role="img" aria-label="Illustration of white vanilla flowers" x="80" y="708" width="162" height="69" rx="30" fill="#e9e6dc" opacity="0.55"/>
  </svg>

  <div class="signature-logo">
    <span class="signature-logo__tagline">Rock Sugar Sticks</span>
    <span class="signature-logo__name">Pebbles</span>
  </div>

</body>
</html>
```